High end building company who specialise in architecturally designed homes needing a presentation do

We need a document/template that can be used in Indesign. We present proposal's, house plans, specifications at various stages throughout a building project from initial contact right through to completion. We want to have the same feel through out each presentation and be able to use the same first few pages and then be able to insert the contents. Sometimes the content will be A4 and other times when presenting plans will be A3. I have attached an example of one previously used for presenting plans (see 01_Conceptual) and one for proposals (see Proposal Example ). The document needs to have a minimalist look and feel very sophisticated to suit our client base. The look of the document should tie in with our logo design which is also attached.

```html
<!DOCTYPE html>
<html lang="en">
<head>
<meta charset="utf-8">
<title>A Message From Miles – Harlow Reid Builders</title>
<link rel="stylesheet" href="https://fonts.googleapis.com/css2?family=EB+Garamond:wght@400&family=Archivo:wght@500;700&display=swap">
<style>
  :root {
    --paper: #f1ece0;
    --paper-warm: #ebe3d2;
    --ink: #2f2d2b;
    --accent: #f26a35;
    --frame: #3a3836;
    --signature-tone: #dcd4c3;
  }
  * { margin: 0; padding: 0; box-sizing: border-box; }
  html, body {
    width: 1200px;
    height: 848px;
    overflow: hidden;
  }
  body { background: var(--paper); }
  .spread {
    position: relative;
    width: 1200px;
    height: 848px;
    background:
      radial-gradient(ellipse at 30% 40%, rgba(255,255,255,0.35), transparent 60%),
      radial-gradient(ellipse at 80% 80%, var(--paper-warm), transparent 70%),
      var(--paper);
    overflow: hidden;
  }

  /* Letter */
  .letter {
    position: absolute;
    left: 92px;
    top: 128px;
    font-family: "EB Garamond", Garamond, serif;
    font-size: 21px;
    line-height: 24px;
    color: var(--ink);
    white-space: nowrap;
  }
  .letter p { margin-bottom: 24px; }
  .letter .salutation { margin-bottom: 32px; }
  .letter .closing { margin-top: 16px; margin-bottom: 0; }

  .signature {
    position: absolute;
    left: 108px;
    top: 576px;
    width: 278px;
    height: 70px;
    border-radius: 4px;
    background: linear-gradient(90deg, var(--signature-tone), rgba(220,212,195,0.4));
  }

  .signatory {
    position: absolute;
    left: 92px;
    top: 670px;
    font-family: "EB Garamond", Garamond, serif;
    font-size: 16.5px;
    line-height: 17.5px;
    color: var(--ink);
  }

  /* Company name */
  .company {
    position: absolute;
    left: 92px;
    top: 745px;
    display: flex;
    align-items: center;
    gap: 11px;
  }
  .company-dot {
    width: 56px;
    height: 56px;
    border-radius: 50%;
    background: var(--ink);
  }
  .company-name {
    font-family: "Archivo", Helvetica, sans-serif;
    font-weight: 500;
    font-size: 20px;
    line-height: 20px;
    letter-spacing: 4px;
    color: var(--ink);
    text-transform: uppercase;
  }

  /* Title panel */
  .title-panel {
    position: absolute;
    left: 907px;
    top: 14px;
    width: 279px;
    height: 278px;
    border: 1px solid var(--frame);
  }
  .title-panel h1 {
    position: absolute;
    right: 29px;
    top: 13px;
    text-align: right;
    font-family: "Archivo", Helvetica, Arial, sans-serif;
    font-weight: 700;
    font-size: 48px;
    line-height: 64px;
    letter-spacing: -2px;
    color: var(--accent);
    text-transform: uppercase;
    white-space: nowrap;
  }
</style>
</head>
<body>
<main class="spread">
  <article class="letter">
    <p class="salutation">Dear Name,</p>
    <p>Lorem ipsum dolor sit amet, consectetuer adipiscing elit.<br>Aenean commodo ligula eget dolor. Aenean massa.</p>
    <p>Cum sociis natoque penatibus et magnis dis parturient<br>montes, nascetur ridiculus mus.</p>
    <p>Donec quam felis, ultricies nec, pellentesque eu, pretium quis,<br>sem. Nulla consequat massa quis enim.</p>
    <p>Donec pede justo, fringilla vel, aliquet nec, vulputate eget,<br>arcu. In enim justo, rhoncus ut, imperdiet a, venenatis vitae,<br>justo. Nullam dictum felis eu pede mollis pretium. Integer</p>
    <p class="closing">Yours Sincerely</p>
  </article>

  <div class="signature" role="img" aria-label="Handwritten signature of the sender"></div>

  <div class="signatory">
    Sample Name<br>Designation
  </div>

  <div class="company">
    <span class="company-dot"></span>
    <span class="company-name">Harlow<br>Reid<br>Builders</span>
  </div>

  <section class="title-panel">
    <h1>A<br>Message<br>From<br>Miles</h1>
  </section>
</main>
</body>
</html>
```